Lead Generating Website Design

We are looking for a brand new design for our existing website.
The existing website is www.brivopartners.com
The website is aimed at businesses that would like to licence the courses from our school to sell themselves.
We want the menu to be the following:
* Home
* About us
* Our Courses
* LMS Platform
* Affiliate Program
* Contact Us
We want the colour scheme to use the following design guide:
https://folioshelf.net/stepsforward/docs/glide_and_wander_brand_guidelines
Like the idea of the circles and colours in the style guide for places. Want lots of white areas as well as coloured areas
An example of a nice looking site is : https://www.studyharbor.online/
MUST look good on mobile also
On the home page we want the following:
A large image with the text :
Over 450 courses written by highly qualified academics with real world experience.
The 'Join our thriving group of Affiliates - start your own online college!' section on the current website with the text and becoming an affiliate video
A section for 'see how our LMS works' with some text and a place for a video
A section for 'About Brivo Remote Learning' with the text Brivo Remote Learning has been providing distance education for over 40 years and have been the leader in online education for over 25 years.
Benefit from the resources and experience of one of the worlds leading course content providers.
Our highly qualified academic staff, HUGE resource library of up to date courses and cutting edge white label LMS enable our affiliates to stay well ahead of their competitors
A section for 'Free information pack' like the one on https://www.studyharbor.online/
Target Market(s)
Education providers looking to licence our courses to sell
Number of Pages Required
1 page
Look and feel

```html
<!DOCTYPE html>
<html lang="en">
<head>
<meta charset="utf-8">
<title>Brivo Remote Learning – Affiliate Program</title>
<link href="https://fonts.googleapis.com/css2?family=Cinzel:wght@400;600&family=Lato:wght@400;700&display=swap" rel="stylesheet">
<style>
:root{
  --blue:#0b5cc5;
  --blue-dark:#0a4ea8;
  --pale:#eef4fb;
  --ink:#2b2b2b;
  --muted:#555;
  --line:#d8dee6;
  --white:#fff;
}
*{box-sizing:border-box;margin:0;padding:0}
html,body{width:1200px;height:3839px;overflow:hidden}
body{position:relative;background:var(--white);font-family:"Lato",sans-serif;color:var(--ink)}
.abs{position:absolute}
.caps{font-family:"Cinzel",serif;font-weight:400}
.btn{display:inline-flex;align-items:center;justify-content:center;background:var(--blue);color:var(--white);font-size:14px;font-weight:700;height:37px;padding:0 20px}
.btn.ghost{background:rgba(255,255,255,.12);border:1px solid rgba(255,255,255,.85)}
.heading-rule{width:82px;height:2px;background:var(--blue);margin-top:10px}
.play{position:absolute;left:50%;top:50%;width:56px;height:56px;margin:-28px 0 0 -28px;border-radius:50%;background:rgba(255,255,255,.92);display:flex;align-items:center;justify-content:center}
.play::after{content:"";border-left:18px solid var(--blue);border-top:11px solid transparent;border-bottom:11px solid transparent;margin-left:5px}

/* top bar */
.topbar{left:0;top:0;width:1200px;height:40px;background:#f4f4f4;font-size:13px;color:#333}
.follow{left:162px;top:0;height:40px;display:flex;align-items:center;gap:8px}
.dot{width:25px;height:25px;border-radius:50%;background:var(--blue)}
.top-contact{right:162px;top:0;height:40px;display:flex;align-items:center;gap:10px}
.ico{width:25px;height:25px;border-radius:50%;background:var(--blue);display:flex;align-items:center;justify-content:center}
.ico svg{width:13px;height:13px}

/* nav */
.nav{left:0;top:40px;width:1200px;height:57px;background:var(--white)}
.brand{left:161px;top:10px;display:flex;align-items:center;gap:8px;color:var(--blue-dark);font-family:"Cinzel",serif;font-size:13px;font-weight:600;line-height:1.15}
.brand-mark{width:16px;height:16px;background:var(--blue)}
.menu{left:395px;top:15px;display:flex;gap:27px;font-family:"Cinzel",serif;font-size:13px;color:#333}
.menu span{padding:4px 7px}
.menu .active{background:var(--blue);color:var(--white)}

/* hero */
.hero{left:0;top:97px;width:1200px;height:503px;background:linear-gradient(180deg,#6b7380 0%,#4b525d 45%,#2f3540 100%)}
.hero h1{position:absolute;left:0;right:0;top:242px;text-align:center;color:var(--white);font-family:"Cinzel",serif;font-weight:400;font-size:31px;line-height:43px;letter-spacing:.5px;text-shadow:0 2px 6px rgba(0,0,0,.5)}
.hero-actions{position:absolute;left:0;right:0;top:347px;display:flex;justify-content:center;gap:22px}
.hero-actions .btn{width:112px}

/* affiliate */
.affiliate{left:0;top:600px;width:1200px;height:547px;background:var(--pale)}
.affiliate .band{left:0;top:0;width:300px;height:547px;background:var(--blue)}
.frame{position:absolute;background:var(--white);padding:8px;box-shadow:0 2px 10px rgba(0,0,0,.12)}
.frame .media{width:100%;height:100%;position:relative}
.affiliate .frame{left:118px;top:75px;width:411px;height:396px}
.affiliate .media{background:linear-gradient(135deg,#ececec,#d6d6d6)}
.aff-copy{left:568px;top:82px;width:468px;font-size:12.5px;color:#333;line-height:27px}
.aff-copy h2{font-family:"Cinzel",serif;font-weight:400;font-size:20px;line-height:31px;color:#222}
.aff-copy .intro{margin-top:20px}
.checks{list-style:none;margin:3px 0 4px}
.checks li{display:flex;align-items:center;gap:9px;font-size:14px;line-height:40px}
.checks svg{width:18px;height:18px}
.aff-copy p.j{text-align:justify;line-height:27px;margin-top:2px}

/* lms */
.lms{left:0;top:1147px;width:1200px;height:715px;background:var(--white)}
.lms h2,.why h2{position:absolute;left:0;right:0;text-align:center;font-family:"Cinzel",serif;font-weight:400;font-size:21px;color:#222}
.lms h2{top:76px}
.center-rule{position:absolute;left:559px;width:82px;height:2px;background:var(--blue)}
.lms .frame{left:161px;top:130px;width:878px;height:441px;padding:8px}
.lms .media{background:linear-gradient(160deg,#8a8a8a 0%,#5a5a5a 55%,#6e5a2e 100%)}
.vbar{position:absolute;left:20px;right:20px;bottom:12px;height:14px;display:flex;align-items:center;gap:10px}
.vbar .track{flex:1;height:4px;background:rgba(255,255,255,.35)}
.vbar .tri{border-left:9px solid #fff;border-top:6px solid transparent;border-bottom:6px solid transparent}
.lms p{position:absolute;left:200px;width:800px;top:598px;text-align:center;font-size:13px;line-height:27px;color:#333}

/* who */
.who{left:0;top:1862px;width:1200px;height:546px;background:var(--pale)}
.who .band{left:900px;top:0;width:300px;height:546px;background:var(--blue)}
.who-copy{left:164px;top:122px;width:470px;font-size:12.5px;line-height:27px;color:#333}
.who-copy h2{font-family:"Cinzel",serif;font-weight:400;font-size:22px;color:#222;line-height:28px}
.who-copy .body{margin-top:18px}
.who-copy .hl{color:var(--blue)}
.who-copy p+p{margin-top:9px}
.who-copy .btn{margin-top:16px;height:36px;padding:0 15px}
.who .frame{left:673px;top:76px;width:412px;height:395px}
.who .media{background:linear-gradient(140deg,#5c4a3e 0%,#9a8a7a 45%,#e8a77a 100%)}

/* interested */
.interested{left:0;top:2408px;width:1200px;height:286px;background:var(--pale)}
.people{left:0;top:0;width:640px;height:286px}
.int-copy{left:679px;top:58px;width:380px;font-size:14px;line-height:30px;color:#333}
.int-copy h2{font-family:"Cinzel",serif;font-weight:400;font-size:21px;line-height:24px;color:#222}
.int-actions{display:flex;align-items:center;gap:20px;margin-top:16px}
.int-actions .btn{height:37px;padding:0 21px}
.phone-big{display:flex;align-items:center;gap:9px;font-size:18px}
.phone-big .ico{width:37px;height:37px}
.phone-big .ico svg{width:17px;height:17px}

/* why */
.why{left:0;top:2694px;width:1200px;height:492px;background:var(--white)}
.why h2{top:76px}
.steps{left:0;top:0;width:1200px;height:260px}
.step-num{position:absolute;width:31px;height:31px;border:1px solid #8aa5c9;border-radius:50%;display:flex;align-items:center;justify-content:center;font-size:13px;color:#446;background:#fff}
.step-label{position:absolute;width:240px;text-align:center;font-size:14px;color:#222}
.dash{position:absolute;height:0;border-top:1px dashed #c4cbd4}
.card{left:162px;top:258px;width:877px;height:159px;border:1px solid var(--line);background:var(--white);box-shadow:0 1px 6px rgba(0,0,0,.06)}
.card .photo{position:absolute;left:9px;top:8px;width:194px;height:143px;background:linear-gradient(135deg,#3a3a3a,#7a6a66 60%,#b44a4a)}
.card ul{position:absolute;left:219px;top:20px;list-style:none;font-size:14px;line-height:30px;color:#222}

/* enquire / contact */
.enquire{left:0;top:3186px;width:600px;height:524px;background:var(--pale)}
.enquire h2,.contact h2{font-family:"Cinzel",serif;font-weight:400;font-size:22px;letter-spacing:.5px}
.enquire h2{position:absolute;left:161px;top:56px;color:#222}
.enquire .lead{position:absolute;left:161px;top:112px;font-size:14px}
.field{position:absolute;left:161px;width:402px;height:33px;border:1px solid #cdd3db;background:var(--white);font-size:12px;color:#777;padding:9px 12px}
.field.msg{height:100px}
.enquire .btn{position:absolute;left:161px;top:427px;width:113px;height:37px}
.contact{left:599px;top:3186px;width:601px;height:524px;background:linear-gradient(120deg,#1f6cd3 0%,#2a74d6 50%,#3b7fd8 100%);color:var(--white)}
.contact h2{position:absolute;left:40px}
.c-row{position:absolute;left:40px;display:flex;align-items:center;gap:10px;font-size:13px;line-height:18px}
.ring{width:31px;height:31px;border:1px solid rgba(255,255,255,.8);border-radius:50%;display:flex;align-items:center;justify-content:center;flex:none}
.ring svg{width:13px;height:13px}

/* footer */
.footer{left:0;top:3710px;width:1200px;height:129px;background:#f4f6f9}
.foot-menu{position:absolute;left:0;right:0;top:38px;display:flex;justify-content:center;gap:40px;font-family:"Cinzel",serif;font-size:13px;color:#333}
.copy{position:absolute;left:0;right:0;top:99px;text-align:center;font-size:11px;color:#444}
</style>
</head>
<body>

<!-- Top bar -->
<div class="abs topbar">
  <div class="abs follow"><span>Follow Us :</span><span class="dot"></span><span class="dot"></span><span class="dot"></span></div>
  <div class="abs top-contact">
    <span class="ico"><svg viewBox="0 0 16 16"><rect x="2" y="4" width="12" height="8" fill="none" stroke="#fff" stroke-width="1.5"/><path d="M2 4l6 5 6-5" fill="none" stroke="#fff" stroke-width="1.5"/></svg></span>
    <span>info@brivoremote.com</span>
    <span style="width:16px"></span>
    <span class="ico"><svg viewBox="0 0 16 16"><path d="M4 2l2.5 3-1.5 1.5c.8 2 2.5 3.7 4.5 4.5L11 9.5l3 2.5-1.5 2C7 14 2 9 2 3.5z" fill="#fff"/></svg></span>
    <span>123 456 789</span>
  </div>
</div>

<!-- Navigation -->
<header class="abs nav">
  <div class="abs brand"><span class="brand-mark"></span><span>Brivo Remote<br>Learning</span></div>
  <nav class="abs menu">
    <span class="active">Home</span><span>About Us</span><span>Our Courses</span><span>LMS Platform</span><span>Affiliate Program</span><span>Contact Us</span>
  </nav>
</header>

<!-- Hero -->
<section class="abs hero" role="img" aria-label="Photo of three students looking at a laptop together">
  <h1>Over 450 courses written by highly qualified<br>academics with real world experience.</h1>
  <div class="hero-actions"><span class="btn">Learn More</span><span class="btn ghost">Contact Us</span></div>
</section>

<!-- Affiliate -->
<section class="abs affiliate">
  <div class="abs band"></div>
  <div class="frame"><div class="media" role="img" aria-label="Video cover: Becoming an Affiliate, with a city skyline illustration"><span class="play"></span></div></div>
  <div class="abs aff-copy">
    <h2>Join Our Thriving Group Of Affiliates -<br>Start Your Own Online College!</h2>
    <div class="heading-rule" style="margin-top:2px"></div>
    <p class="intro">No previous education experience required - tutors are available.</p>
    <ul class="checks">
      <li><svg viewBox="0 0 18 18"><circle cx="9" cy="9" r="7.5" fill="none" stroke="#0b5cc5" stroke-width="1.4"/><path d="M5.5 9.2l2.4 2.4 5-5.5" fill="none" stroke="#0b5cc5" stroke-width="1.6"/></svg>Are you looking for a new business venture?</li>
      <li><svg viewBox="0 0 18 18"><circle cx="9" cy="9" r="7.5" fill="none" stroke="#0b5cc5" stroke-width="1.4"/><path d="M5.5 9.2l2.4 2.4 5-5.5" fill="none" stroke="#0b5cc5" stroke-width="1.6"/></svg>Do you want to be your own boss?</li>
      <li><svg viewBox="0 0 18 18"><circle cx="9" cy="9" r="7.5" fill="none" stroke="#0b5cc5" stroke-width="1.4"/><path d="M5.5 9.2l2.4 2.4 5-5.5" fill="none" stroke="#0b5cc5" stroke-width="1.6"/></svg>Do you want to earn a great income, and still have a life?</li>
    </ul>
    <p class="j">You might already be working in education, or perhaps you're part of an association that is looking to expand it's offerings to it's members, or, just a motivated business person!</p>
    <p class="j" style="margin-top:6px">Don't reinvent the wheel - our business model works - and it's an affordable buy in.</p>
  </div>
</section>

<!-- LMS -->
<section class="abs lms">
  <h2>How Our LMS Works</h2>
  <div class="center-rule" style="top:110px"></div>
  <div class="frame"><div class="media" role="img" aria-label="Video still of a student working at a desk with a computer and notebook"><span class="play"></span>
    <div class="vbar"><span class="tri"></span><span class="track"></span></div></div></div>
  <p>Lorem Ipsum is simply dummy text of the printing and typesetting industry. Lorem Ipsum has been the industry's standard dummy text ever since the 1500s, when an unknown printer took a galley of type and scrambled it to make a type specimen book.</p>
</section>

<!-- Who we are -->
<section class="abs who">
  <div class="abs band"></div>
  <div class="abs who-copy">
    <h2>WHO ARE BRIVO REMOTE LEARNING</h2>
    <div class="heading-rule"></div>
    <div class="body">
      <p>Brivo Remote Learning has been providing distance education for over <span class="hl">40 years</span> and have been the leader in online education for over <span class="hl">25 years</span>.<br>Benefit from the resources and experience of one of the worlds leading course content providers.</p>
      <p>Our highly qualified academic staff, HUGE resource library of up to date courses and cutting edge white label LMS enable our affiliates to stay well ahead of their competitors</p>
    </div>
    <span class="btn">More About Brivo Remote Learning</span>
  </div>
  <div class="frame"><div class="media" role="img" aria-label="Video cover: hands typing on a laptop showing the school's course promotion"><span class="play"></span></div></div>
</section>

<!-- Interested -->
<section class="abs interested">
  <svg class="abs people" viewBox="0 0 640 286" role="img" aria-label="Photo of a group of smiling students walking with books">
    <defs><linearGradient id="crowd" x1="0" y1="0" x2="1" y2="1"><stop offset="0" stop-color="#8a7a6a"/><stop offset=".5" stop-color="#3d4a66"/><stop offset="1" stop-color="#6a6f7a"/></linearGradient></defs>
    <polygon points="0,0 585,0 638,143 585,286 0,286" fill="url(#crowd)"/>
    <polyline points="585,0 638,143 585,286" fill="none" stroke="#0b5cc5" stroke-width="4"/>
  </svg>
  <div class="abs int-copy">
    <h2>Interested in becoming<br>an affiliate?</h2>
    <p style="margin-top:2px">Contact us now to discuss how we can work together to launch your own Distance Education Business...</p>
    <div class="int-actions"><span class="btn">Contact Us</span>
      <span class="phone-big"><span class="ico"><svg viewBox="0 0 16 16"><path d="M4 2l2.5 3-1.5 1.5c.8 2 2.5 3.7 4.5 4.5L11 9.5l3 2.5-1.5 2C7 14 2 9 2 3.5z" fill="#fff"/></svg></span>123 456 789</span></div>
  </div>
</section>

<!-- Why choose us -->
<section class="abs why">
  <h2>Why Choose Us</h2>
  <div class="center-rule" style="top:110px"></div>
  <div class="abs steps">
    <span class="dash" style="left:273px;top:161px;width:60px"></span>
    <span class="dash" style="left:400px;top:161px;width:80px"></span>
    <span class="dash" style="left:527px;top:161px;width:60px"></span>
    <span class="dash" style="left:660px;top:161px;width:85px"></span>
    <span class="dash" style="left:791px;top:161px;width:60px"></span>
    <span class="step-num" style="left:226px;top:146px">1</span>
    <span class="step-num" style="left:481px;top:146px">2</span>
    <span class="step-num" style="left:745px;top:146px">3</span>
    <svg class="abs" style="left:338px;top:126px" width="60" height="62" viewBox="0 0 60 62" fill="none" stroke="#0b5cc5" stroke-width="2"><rect x="4" y="6" width="24" height="36"/><rect x="30" y="6" width="24" height="36"/><rect x="9" y="14" width="14" height="10"/><path d="M14 17l5 2-5 2z"/><path d="M9 30h14M9 35h14M35 16h14M35 22h14"/><path d="M38 58V34a3 3 0 016 0v10l8 2v12"/></svg>
    <svg class="abs" style="left:604px;top:126px" width="46" height="60" viewBox="0 0 46 60" fill="none" stroke="#333" stroke-width="2"><rect x="4" y="3" width="38" height="52" rx="2"/><path d="M4 46h38M18 3v18l5-4 5 4V3"/></svg>
    <svg class="abs" style="left:868px;top:124px" width="56" height="62" viewBox="0 0 56 62" fill="none" stroke="#333" stroke-width="2"><circle cx="28" cy="24" r="13"/><path d="M12 24a16 16 0 0132 0M12 22v8h4v-8zM44 22v8h-4v-8zM40 30c0 6-6 8-10 8"/><path d="M6 60c0-12 10-18 22-18s22 6 22 18z"/></svg>
    <span class="step-label" style="left:247px;top:214px">Delivering Our Courses</span>
    <span class="step-label" style="left:506px;top:214px">Selling Our Ebooks</span>
    <span class="step-label" style="left:776px;top:214px">Extra Support Available</span>
  </div>
  <div class="abs card">
    <div class="photo" role="img" aria-label="Photo of a student studying with a laptop and notebook"></div>
    <ul>
      <li>Systems allow delivery online, on USB Stick or with printed notes.</li>
      <li>Over 600 courses, over 25 million words of intellectual property.</li>
      <li>Latest course versions accessed via a cloud based repository</li>
      <li>Royalties paid monthly</li>
    </ul>
  </div>
</section>

<!-- Enquire -->
<section class="abs enquire">
  <h2>ENQUIRE</h2>
  <div class="abs" style="left:161px;top:88px;width:82px;height:2px;background:var(--blue)"></div>
  <p class="lead">Get Free Access To Our Info Packs</p>
  <div class="field" style="top:149px">Name</div>
  <div class="field" style="top:201px">Email</div>
  <div class="field" style="top:253px">Phone</div>
  <div class="field msg" style="top:305px">Message</div>
  <span class="btn">Submit Now</span>
</section>

<!-- Contact -->
<section class="abs contact" role="img" aria-label="Blue tinted photo of a smiling student with a backpack">
  <h2 style="top:56px">Contact Details</h2>
  <div class="c-row" style="top:115px"><span class="ring"><svg viewBox="0 0 16 16"><path d="M8 1a5 5 0 00-5 5c0 4 5 9 5 9s5-5 5-9a5 5 0 00-5-5z" fill="#fff"/><circle cx="8" cy="6" r="2" fill="#2a74d6"/></svg></span><span>123, Lorem Ipsum Dolar sit,<br>123, Lorem Ipsum Dolar Sit Amet</span></div>
  <div class="c-row" style="top:168px"><span class="ring"><svg viewBox="0 0 16 16"><rect x="2" y="4" width="12" height="8" fill="none" stroke="#fff" stroke-width="1.5"/><path d="M2 4l6 5 6-5" fill="none" stroke="#fff" stroke-width="1.5"/></svg></span><span>info@brivoremote.com</span></div>
  <div class="c-row" style="top:221px;font-size:17px"><span class="ring"><svg viewBox="0 0 16 16"><path d="M4 2l2.5 3-1.5 1.5c.8 2 2.5 3.7 4.5 4.5L11 9.5l3 2.5-1.5 2C7 14 2 9 2 3.5z" fill="#fff"/></svg></span><span>123 456 789</span></div>
  <h2 style="top:292px">Social Media</h2>
  <div class="c-row" style="top:352px;font-size:14px"><span class="ring"></span><span>Circlebook</span></div>
  <div class="c-row" style="top:396px;font-size:14px"><span class="ring"></span><span>Chirpline</span></div>
  <div class="c-row" style="top:443px;font-size:14px"><span class="ring"></span><span>WorkLinked</span></div>
</section>

<!-- Footer -->
<footer class="abs footer">
  <div class="foot-menu"><span>Home</span><span>About Us</span><span>Our Courses</span><span>LMS Platform</span><span>Affiliate Program</span><span>Contact Us</span></div>
  <div class="copy">Copyright 2021. Brivo Remote Learning. All Rights Reserved</div>
</footer>

</body>
</html>
```